Organic Soap Packaging

We need a package design for a new company called Willow Naturals. Our primary product is organic soap. Our business model is based on the social entrepreneurial concept of by one give one like Brend shoes. We are giving soap to help prevent the spread of disease; 1.4 million deaths a year can be prevented by hand washing.

The design is for a recycled cardboard box/package. We want to demonstrate the high end, luxury feel of the product with undertones of organic/earth friendly/social conscious.

The soap is small batch, spa like, essential oil scented all natural luxury.
Updates

I am very excited about this startup business and I believe we will have great success! I am passionate about organic personal care and helping others in need. If you share my passion, please bring your work to the table!

Target Market(s)

My target market is people who are educated through college. Health conscious, socially conscious, Generation X. Basically shoppers of Green Basket and Haverline.

Industry/Entity Type

Business

Requirements
Must have
• Suitable for Face, Hair, and Skin
Scented with Organic Essential Oils

```html
<!DOCTYPE html>
<html lang="en">
<head>
<meta charset="utf-8">
<title>Willow Naturals – Soap Box Dieline</title>
<link rel="stylesheet" href="https://fonts.googleapis.com/css2?family=Vollkorn:wght@600&family=Open+Sans:wght@400&family=Delius&family=Arimo&display=swap">
<style>
  :root {
    --backdrop: #7b7b7b;
    --board-top: #ffffff;
    --board-bottom: #ecf4cc;
    --crease: #d9d9d9;
    --brand: #5f7f33;
    --seal-ink: #4d7a16;
    --seal-ring: #7f9a4a;
    --claim-ink: #8a8a8a;
    --copy-ink: #8c8c8c;
    --leaf-light: #e2eebc;
    --leaf-mid: #b9d48a;
    --leaf-deep: #93ad6a;
  }
  * { margin: 0; padding: 0; box-sizing: border-box; }
  html, body { width: 1200px; height: 1131px; overflow: hidden; background: var(--backdrop); }
  .dieline { position: relative; width: 1200px; height: 1131px; }
  .dieline__shapes { position: absolute; inset: 0; }
  .front-panel, .top-band { position: absolute; left: 248px; width: 696px; }
  .front-panel { height: 349px; }
  .top-band { height: 161px; }
  .front-panel--upper { top: 52px; }
  .front-panel--lower { top: 567px; }
  .top-band--upper { top: 404px; }
  .top-band--lower { top: 917px; }
  .artwork {
    position: absolute; left: 3px; top: 29px; width: 323px; height: 318px;
    background: radial-gradient(ellipse at 20% 85%, var(--leaf-mid) 0%, var(--leaf-light) 55%, rgba(236,244,204,0) 80%);
  }
  .brand-name {
    position: absolute; font-family: "Vollkorn", serif; font-weight: 600;
    color: var(--brand); white-space: nowrap; line-height: 1;
  }
  .front-panel .brand-name { right: 41px; top: 33px; font-size: 54px; }
  .top-band .brand-name { left: 37px; top: 63px; font-size: 33px; }
  .scent-seal {
    position: absolute; left: 365px; top: 109px; width: 292px; height: 73px;
    border: 2px solid var(--seal-ring); border-radius: 50%; background: rgba(255,255,255,0.6);
    display: flex; align-items: center; justify-content: center;
    font-family: "Delius", cursive; font-size: 14px; color: var(--seal-ink);
  }
  .use-claim {
    position: absolute; left: 367px; top: 308px;
    font-family: "Open Sans", sans-serif; font-size: 18px; color: var(--claim-ink); letter-spacing: 0.3px;
  }
  .ingredients {
    position: absolute; left: 333px; top: 42px; width: 350px;
    font-family: "Arimo", sans-serif; font-size: 13.6px; line-height: 18.8px; color: var(--copy-ink);
  }
</style>
</head>
<body>
<main class="dieline">
  <svg class="dieline__shapes" width="1200" height="1131" viewBox="0 0 1200 1131">
    <defs>
      <linearGradient id="board" x1="0" y1="0" x2="0" y2="1">
        <stop offset="0" stop-color="#ffffff"/>
        <stop offset="1" stop-color="#ecf4cc"/>
      </linearGradient>
    </defs>
    <g fill="url(#board)" stroke="#d9d9d9" stroke-width="2">
      <rect x="248" y="52" width="696" height="349"/>
      <rect x="944" y="52" width="158" height="349"/>
      <path d="M1102 52 H1150 Q1180 52 1180 82 V371 Q1180 401 1150 401 H1102 Z"/>
      <polygon points="84,431 248,404 248,565 84,561"/>
      <rect x="248" y="404" width="696" height="161"/>
      <polygon points="944,404 1108,404 1108,541 944,565"/>
      <path d="M84 567 H36 Q7 567 7 596 V888 Q7 917 36 917 H84 Z"/>
      <rect x="84" y="567" width="164" height="350"/>
      <rect x="248" y="567" width="696" height="350"/>
      <polygon points="84,917 248,917 248,1080 84,1056"/>
      <rect x="248" y="917" width="696" height="163"/>
      <polygon points="944,917 1108,940 1108,1080 944,1080"/>
    </g>
  </svg>

  <section class="front-panel front-panel--upper">
    <div class="artwork" role="img" aria-label="Green floral illustration of flowers, swirls and leaves"></div>
    <h1 class="brand-name">Willow Naturals</h1>
    <p class="scent-seal">Scented with Organic Essential Oils</p>
    <p class="use-claim">Suitable for Face, Hair, and Skin</p>
  </section>

  <section class="top-band top-band--upper">
    <p class="brand-name">Willow Naturals</p>
    <p class="ingredients">Ingredients: Water, organic coconut*, potassium hydroxide**, organic olive oil*, organic orange oil, organic hemp oil, organic jojoba oil, organic lemon oil, organic lime oil, citric acid, tocopherol.</p>
  </section>

  <section class="front-panel front-panel--lower">
    <div class="artwork" role="img" aria-label="Green floral illustration of flowers, swirls and leaves"></div>
    <p class="brand-name">Willow Naturals</p>
    <p class="scent-seal">Scented with Organic Essential Oils</p>
    <p class="use-claim">Suitable for Face, Hair, and Skin</p>
  </section>

  <section class="top-band top-band--lower">
    <p class="brand-name">Willow Naturals</p>
    <p class="ingredients">Ingredients: Water, organic coconut*, potassium hydroxide**, organic olive oil*, organic orange oil, organic hemp oil, organic jojoba oil, organic lemon oil, organic lime oil, citric acid, tocopherol.</p>
  </section>
</main>
</body>
</html>
```